VELUNDO Brisbane Tiling Service

My name is Mirko Bostel i need a business card for a new company. We are wall and floor tilers based in Brisbane, our company is Velundio Brisbane Tiling Service.
We would like a logo from our website used on our cards. Our website is www.velundio.com.au

I would like my Facebook and Twitter accounts on my card.

Industry/Entity Type

Business

Colors
0692cd
3176b5
33a6d7
85cae6

```html
<!DOCTYPE html>
<html lang="en">
<head>
<meta charset="utf-8">
<title>Velundo Brisbane Tiling Service – Business Card</title>
<link rel="stylesheet" href="https://fonts.googleapis.com/css2?family=Jost:wght@400&display=swap">
<style>
  :root {
    --brand-blue: #1f74c0;
    --mark-blue: #2f8fd8;
    --mark-edge: #1d6fb8;
    --ink: #111111;
    --rule: #c5cbcb;
    --divider: #8a9494;
    --green: #5cf08f;
    --orange: #fb9a2b;
    --red: #f2383f;
    --blue: #3c8be9;
    --purple: #7a3df0;
    --icon-person: #4a9de0;
    --icon-chair: #8b3fe0;
    --icon-phone: #2fd045;
    --icon-pin: #ee2e3a;
    --icon-mail: #f2c31b;
    --icon-globe: #2a3d5a;
    --icon-square-a: #3f7ff2;
    --icon-square-b: #6fe0ee;
    --paper: #ffffff;
  }
  * { margin: 0; padding: 0; box-sizing: border-box; }
  html, body { width: 1200px; height: 720px; overflow: hidden; background: var(--paper); }
  .card {
    position: relative;
    width: 1200px;
    height: 720px;
    background: var(--paper);
    font-family: "Jost", "Futura", sans-serif;
    overflow: hidden;
  }
  .card__frame { position: absolute; inset: 0; width: 1200px; height: 720px; }
  .brand { position: absolute; left: 43px; top: 226px; display: flex; align-items: center; }
  .brand__square {
    width: 231px; height: 237px;
    background: var(--mark-blue);
    border: 6px solid var(--mark-edge);
    border-radius: 10px;
  }
  .brand__name {
    position: absolute;
    left: 262px;
    top: -16px;
    color: var(--brand-blue);
    font-size: 56px;
    line-height: 68px;
    text-transform: uppercase;
    white-space: nowrap;
  }
  .details { position: absolute; left: 638px; width: 544px; top: 0; height: 720px; }
  .row {
    position: absolute;
    left: 0; right: 0;
    height: 40px;
    display: flex;
    align-items: center;
    justify-content: flex-end;
    color: var(--ink);
    font-size: 27px;
    text-transform: uppercase;
    white-space: nowrap;
  }
  .row--name { font-size: 36px; height: 46px; }
  .row__icon { position: absolute; left: 10px; top: 50%; transform: translateY(-50%); width: 30px; height: 30px; }
  .rule { position: absolute; left: 0; right: 0; height: 4px; background: var(--rule); }
</style>
</head>
<body>
<main class="card">
  <svg class="card__frame" viewBox="0 0 1063 627" preserveAspectRatio="none" aria-hidden="true">
    <polygon points="0,17 595,17 584,28 0,28" fill="var(--green)"/>
    <polygon points="0,28 584,28 571,40 0,40" fill="var(--orange)"/>
    <polygon points="0,40 571,40 558,52 0,52" fill="var(--red)"/>
    <polygon points="0,52 558,52 545,64 0,64" fill="var(--blue)"/>
    <polygon points="0,64 545,64 531,77 0,77" fill="var(--purple)"/>
    <rect x="529" y="77" width="3" height="486" fill="var(--divider)"/>
    <polygon points="531,563 1063,563 1063,575 520,575" fill="var(--purple)"/>
    <polygon points="520,575 1063,575 1063,587 507,587" fill="var(--blue)"/>
    <polygon points="507,587 1063,587 1063,599 495,599" fill="var(--red)"/>
    <polygon points="495,599 1063,599 1063,611 483,611" fill="var(--orange)"/>
    <polygon points="483,611 1063,611 1063,623 471,623" fill="var(--green)"/>
  </svg>

  <section class="brand">
    <div class="brand__square"></div>
    <h1 class="brand__name">Velundo<br>Brisbane<br>Tiling<br>Service</h1>
  </section>

  <section class="details">
    <div class="row row--name" style="top:84px">
      <svg class="row__icon" viewBox="0 0 30 30"><circle cx="15" cy="9" r="6" fill="var(--icon-person)"/><path d="M3 28c0-8 5-12 12-12s12 4 12 12z" fill="var(--icon-person)"/></svg>
      Dinesh Karvell
    </div>
    <div class="row" style="top:140px">
      <svg class="row__icon" viewBox="0 0 30 30"><rect x="9" y="2" width="12" height="13" rx="2" fill="var(--icon-chair)"/><rect x="6" y="15" width="18" height="4" fill="var(--icon-chair)"/><rect x="14" y="19" width="2" height="6" fill="var(--icon-chair)"/><rect x="7" y="25" width="16" height="2" fill="var(--icon-chair)"/></svg>
      CEO, Founder
    </div>
    <div class="rule" style="top:186px"></div>
    <div class="row" style="top:195px">
      <svg class="row__icon" viewBox="0 0 30 30"><path d="M7 3l5 0 2 7-3 3c2 4 4 6 7 7l3-3 7 2 0 5c0 2-2 3-4 3C13 27 3 17 3 7c0-2 2-4 4-4z" fill="var(--icon-phone)"/></svg>
      +91 9012457836
    </div>
    <div class="row" style="top:251px">+91 9075318264</div>
    <div class="rule" style="top:299px"></div>
    <div class="row" style="top:307px">
      <svg class="row__icon" viewBox="0 0 30 30" style="height:38px"><path d="M15 29C9 20 5 15 5 10a10 10 0 0 1 20 0c0 5-4 10-10 19z" fill="var(--icon-pin)"/><circle cx="15" cy="10" r="4" fill="var(--paper)"/></svg>
      Your address your address
    </div>
    <div class="row" style="top:362px">Your address your address</div>
    <div class="rule" style="top:409px"></div>
    <div class="row" style="top:421px">
      <svg class="row__icon" viewBox="0 0 30 30"><rect x="2" y="7" width="26" height="17" fill="var(--icon-mail)"/><path d="M2 7l13 10 13-10" fill="none" stroke="var(--paper)" stroke-width="2"/></svg>
      youremail@email.com
    </div>
    <div class="rule" style="top:469px"></div>
    <div class="row" style="top:479px">
      <svg class="row__icon" viewBox="0 0 30 30"><circle cx="15" cy="15" r="12" fill="var(--icon-globe)"/><path d="M15 3v24M3 15h24" stroke="var(--paper)" stroke-width="1.5"/></svg>
      www.website.com
    </div>
    <div class="rule" style="top:527px"></div>
    <div class="row" style="top:540px">
      <svg class="row__icon" viewBox="0 0 30 30"><rect x="3" y="3" width="24" height="24" fill="var(--icon-square-a)"/></svg>
      FB/tilebloke
    </div>
    <div class="rule" style="top:589px"></div>
    <div class="row" style="top:600px">
      <svg class="row__icon" viewBox="0 0 30 30"><rect x="3" y="3" width="24" height="24" fill="var(--icon-square-b)"/></svg>
      Twitter/@profile
    </div>
  </section>
</main>
</body>
</html>
```